Commercial LED Lighting Company need Product Catalog

We need a product catalog for our commercial LED Lighting company. We sell indoor and outdoor lighting fixtures to commercial customers, for commercial purposes. Most of our clients are knowledgeable about our products, and are interested in the technical details of our products.

Our catalog will offer 17 products, with a two page layout for each product. We have a specific vision for the general outline of the product layout. Attached, you will see a competitor's design whose layout we'd like to mimic - the first page for a product will have a large photo up top of a room or space showcasing the product, and the bottom half will be a photo of the product with some general bullet points. The second page will list the various model numbers for the products, along with their technical details. All information needed for the project will be provided, including product photos. We will not include all product photos in our attachment today, as we are limited to how many files we can upload at this time. Also attached is a general outline of the catalog, as well as product details.

Our clients are professionals, and we want to communicate a respect for our clients' know how and industry experience. We also want to maintain our color palate of blue, white and grey. I will also attach our logo to give you a reference.

Sample designs should include a potential cover design, and a two page layout for a single product.

Target Market(s)

LED Lighting Distributors; engineers; professional customers

Industry/Entity Type

Manufacturer

Font styles to use
Sans Serif

Colors
0355a3
cfdeed
85acd3
3276b5
eaf1f7

Requirements
Must have
• All required technical information as outlined in attached documents; all 17 products; the two page layout we have envisioned; our color scheme.

```html
<!DOCTYPE html>
<html lang="en">
<head>
<meta charset="utf-8">
<title>Norvale Lighting – Catalog Cover</title>
<link rel="stylesheet" href="https://fonts.googleapis.com/css2?family=Open+Sans:wght@400;700;800&display=swap">
<style>
  :root {
    --brand-blue: #0355a3;
    --mid-blue: #3276b5;
    --sky-blue: #1fa8e0;
    --pale-blue: #cfdeed;
    --mist-blue: #eaf1f7;
    --soft-blue: #85acd3;
    --paper: #ffffff;
    --stage: #2b2b2b;
    --photo-warm: #c9b8a2;
    --photo-dark: #3e3a36;
  }
  * { box-sizing: border-box; margin: 0; padding: 0; }
  html, body {
    width: 1200px; height: 900px; overflow: hidden;
    background: var(--stage);
    font-family: "Open Sans", Arial, sans-serif;
  }
  .cover {
    position: absolute; left: 100px; top: 100px;
    width: 1000px; height: 700px;
    background: var(--paper);
    overflow: hidden;
  }
  .cover-art { position: absolute; inset: 0; }
  .values {
    position: absolute; list-style: none;
    color: var(--sky-blue); font-weight: 700;
    font-size: 40px; letter-spacing: 1px; line-height: 1;
  }
  .values li { position: absolute; white-space: nowrap; }
  .values .v-quality { left: 655px; top: 120px; }
  .values .v-service { left: 625px; top: 195px; }
  .values .v-style   { left: 595px; top: 270px; }
  .brand {
    position: absolute; left: 610px; top: 385px;
    display: flex; align-items: center; gap: 16px;
  }
  .brand-dot {
    flex: 0 0 68px;
    width: 68px; height: 68px; border-radius: 50%;
    background: var(--brand-blue);
  }
  .brand-text { display: flex; flex-direction: column; }
  .brand-name {
    color: var(--brand-blue); font-weight: 800;
    font-size: 36px; line-height: 1; letter-spacing: 0.5px;
  }
  .brand-name span { display: block; white-space: nowrap; }
  .brand-tagline {
    color: var(--brand-blue); font-weight: 400;
    font-size: 15px; margin-top: 6px; white-space: nowrap;
  }
  .web-link {
    position: absolute; left: 512px; top: 561px;
    transform: rotate(-4.8deg); transform-origin: left center;
    color: var(--paper); font-size: 24px; font-weight: 400;
    white-space: nowrap;
  }
</style>
</head>
<body>
  <section class="cover">
    <svg class="cover-art" viewBox="0 0 1000 700" width="1000" height="700">
      <defs>
        <linearGradient id="roomTone" x1="0" y1="0" x2="1" y2="1">
          <stop offset="0" stop-color="#eef0f2"/>
          <stop offset="0.45" stop-color="#c9b8a2"/>
          <stop offset="0.8" stop-color="#3e3a36"/>
          <stop offset="1" stop-color="#5b55c8"/>
        </linearGradient>
        <linearGradient id="paperFade" x1="0" y1="0" x2="1" y2="0">
          <stop offset="0" stop-color="#f1f4f7"/>
          <stop offset="1" stop-color="#ffffff"/>
        </linearGradient>
      </defs>
      <rect class="paper-ground" x="0" y="0" width="1000" height="700" fill="url(#paperFade)"/>
      <polygon class="room-photo" role="img" aria-label="Modern kitchen interior with pendant lights and blue LED accent lighting"
               points="0,0 560,0 330,700 0,700" fill="url(#roomTone)"/>
      <polygon class="stripe-sky" points="505,0 520,0 290,700 275,700" fill="var(--sky-blue)"/>
      <polygon class="stripe-brand" points="575,0 640,0 410,700 345,700" fill="var(--brand-blue)"/>
      <polygon class="stripe-mid" points="655,0 670,0 440,700 425,700" fill="var(--mid-blue)" opacity="0.85"/>
      <polygon class="web-band" points="470,550 1000,505 1000,555 455,605" fill="var(--brand-blue)"/>
      <polygon class="web-band-edge" points="455,605 1000,555 1000,565 452,615" fill="var(--sky-blue)"/>
      <g class="globe-icon" transform="translate(488,580)" fill="none" stroke="#ffffff" stroke-width="2">
        <circle r="10"/>
        <ellipse rx="4.5" ry="10"/>
        <line x1="-10" y1="0" x2="10" y2="0"/>
      </g>
    </svg>

    <ul class="values">
      <li class="v-quality">QUALITY</li>
      <li class="v-service">SERVICE</li>
      <li class="v-style">STYLE</li>
    </ul>

    <div class="brand">
      <span class="brand-dot"></span>
      <div class="brand-text">
        <span class="brand-name"><span>NORVALE</span><span>LIGHTING</span></span>
        <span class="brand-tagline">Built for Commercial Spaces</span>
      </div>
    </div>

    <div class="web-link">www.norvalelighting.com</div>
  </section>
</body>
</html>
```